Mother's Day Sale Banner Ad For Jewelry Site

We are looking for a designer to design a banner on our website advertising our Mother's Day Sale. I have enclosed a few pieces of jewelry we would like used in the ad. The ad size needs to be 1187 × 400. The ad should say:

Mother's Day Sale - Save 15% with Promo Code: LOVEMOM

```html
<!DOCTYPE html>
<html lang="en">
<head>
<meta charset="UTF-8">
<title>Mother's Day Sale</title>
<link rel="stylesheet" href="https://fonts.googleapis.com/css2?family=Raleway:wght@400;500;600&display=swap">
<style>
  :root {
    --bg-left: #f3f3f3;
    --bg-right: #f6f3e8;
    --navy: #2c3142;
    --ink: #111111;
    --red: #d42f38;
    --label-bg: #fbf3d6;
    --frame: #e3d6ae;
    --tile-light: #ffffff;
    --tile-warm: #f1eee6;
  }
  * { margin: 0; padding: 0; box-sizing: border-box; }
  html, body { width: 1200px; height: 404px; overflow: hidden; }
  .banner {
    position: relative;
    width: 1200px;
    height: 404px;
    background: linear-gradient(90deg, var(--bg-left) 0%, #f7f6f2 55%, var(--bg-right) 80%, #fbfaf6 100%);
    font-family: "Raleway", sans-serif;
    overflow: hidden;
  }
  .sale-label {
    position: absolute;
    left: 113px; top: 70px;
    width: 424px; height: 41px;
    background: var(--label-bg);
    color: var(--navy);
    font-weight: 500;
    font-size: 26px;
    letter-spacing: 3px;
    line-height: 41px;
    text-align: center;
  }
  .save-line {
    position: absolute;
    left: 220px; top: 140px;
    font-size: 54px;
    font-weight: 400;
    color: var(--ink);
    line-height: 60px;
    white-space: nowrap;
  }
  .save-line .percent { color: var(--red); font-weight: 500; }
  .promo-line {
    position: absolute;
    left: 148px; top: 200px;
    font-size: 40px;
    color: var(--ink);
    line-height: 48px;
    white-space: nowrap;
  }
  .promo-code {
    position: absolute;
    left: 131px; top: 256px;
    font-size: 76px;
    font-weight: 500;
    color: var(--red);
    letter-spacing: 5px;
    line-height: 84px;
    white-space: nowrap;
  }
  .tile {
    position: absolute;
    width: 124px; height: 124px;
    transform: rotate(45deg);
    border-radius: 6px;
    border: 2px solid var(--frame);
    background: radial-gradient(circle at 50% 50%, var(--tile-light) 0%, var(--tile-warm) 100%);
    box-shadow: 0 2px 6px rgba(120, 100, 60, 0.18), inset 0 0 0 4px #ffffff;
  }
  .tile-top    { left: 848px; top: 35px; }
  .tile-left   { left: 729px; top: 138px; }
  .tile-right  { left: 926px; top: 138px; }
  .tile-bottom { left: 832px; top: 240px; }
</style>
</head>
<body>
  <main class="banner">
    <div class="sale-label">MOTHER’S DAY SALE</div>
    <div class="save-line">Save <span class="percent">15%</span></div>
    <div class="promo-line">with Promo Code:</div>
    <div class="promo-code">LOVEMOM</div>

    <div class="tile tile-top" role="img" aria-label="Gold and diamond lattice band ring"></div>
    <div class="tile tile-left" role="img" aria-label="Pair of gold rope rings with diamond X detail"></div>
    <div class="tile tile-right" role="img" aria-label="Gold ring set with carved coral"></div>
    <div class="tile tile-bottom" role="img" aria-label="Gold crab brooch set with rubies"></div>
  </main>
</body>
</html>
```